Business Card Design Project

I own a dental practice and would like to use a logo that was recently designed to make business cards.
I am looking for a clean card with the following information on the card.

Halvorsen Dental Center (Using the logo)
Martin L. Halvorsen, D.D.S.
7234 Pinewick Ave. Suite B
Colorado Springs, CO 80547
(719) 482-6130
halvorsendentalcenter@mailbox-example.net
www.halvorsendentalcenter.example

Also a list of items on the back:
Services include

Family Dentistry
Cosmetic
Whitening
Tooth Colored Fillings
Crowns/Bridges
Implants/Tooth Replacement
Dentures
Root Canals
Updates

Just an FYI, I added an email address and website address.

I also added my Pic.  Please give designs with and without the pic

Thanks

Target Market(s)

20-70 U.S. Female that handles the household budget.

Industry/Entity Type

Dental

Requirements
Must have
• The logo is key. The color scheme of the logo is also key. The back of the business card should have the list of Dental Services offered at the practice. The front should be clean and professional looking. No cartoons. I will also include a picture of myself. I think that the final card may or may not include this picture, so the card designs should come with and without the picture. USE THE BLUE LOGO ONLY!!!
Should not have
• NO teeth should be on the card.

```html
<!DOCTYPE html>
<html lang="en">
<head>
<meta charset="utf-8">
<title>Halvorsen Dental Center – Business Cards</title>
<link rel="stylesheet" href="https://fonts.googleapis.com/css2?family=Montserrat:wght@400;500;600&display=swap">
<style>
  :root {
    --bg: #e6e8ea;
    --card: #ffffff;
    --teal: #1f6f8b;
    --text-blue: #2b7596;
    --brand-brown: #7b6b5d;
    --white: #ffffff;
  }
  * { box-sizing: border-box; margin: 0; padding: 0; }
  html, body { width: 1200px; height: 900px; overflow: hidden; }
  body {
    background: var(--bg);
    font-family: "Montserrat", sans-serif;
    position: relative;
  }
  .card {
    position: absolute;
    top: 296px;
    width: 540px;
    height: 309px;
    background: var(--card);
    border-radius: 22px;
    overflow: hidden;
    box-shadow: 0 6px 20px rgba(0,0,0,0.12);
  }
  .card--back { left: 40px; }
  .card--front { left: 620px; }

  .card-band { position: absolute; inset: 0; width: 100%; height: 100%; }

  .brand {
    position: absolute;
    display: flex;
    align-items: center;
    gap: 10px;
  }
  .brand-dot {
    width: 16px; height: 16px;
    border-radius: 50%;
    background: var(--teal);
    flex: none;
  }
  .brand-name {
    font-weight: 500;
    font-size: 21px;
    color: var(--brand-brown);
    white-space: nowrap;
  }
  .card--back .brand { left: 70px; top: 62px; }
  .card--front .brand { left: 150px; top: 46px; }

  .services {
    position: absolute;
    left: 0; right: 0;
    top: 176px;
    text-align: center;
    color: var(--white);
    font-size: 15px;
    line-height: 25px;
    letter-spacing: 0.2px;
  }

  .doctor {
    position: absolute;
    left: 236px; top: 106px;
    font-size: 17px;
    color: var(--text-blue);
    letter-spacing: 0.4px;
    white-space: nowrap;
  }
  .contact {
    position: absolute;
    left: 236px; top: 138px;
    list-style: none;
    font-size: 12px;
    line-height: 21px;
    color: var(--text-blue);
    white-space: nowrap;
  }
  .contact b { font-weight: 600; margin-right: 5px; }
  .address {
    position: absolute;
    left: 30px; bottom: 26px;
    display: flex;
    gap: 8px;
    font-style: normal;
    font-size: 16px;
    line-height: 22px;
    color: var(--text-blue);
    white-space: nowrap;
  }
  .address svg { margin-top: 4px; flex: none; }
</style>
</head>
<body>

  <section class="card card--back" aria-label="Card back – services">
    <svg class="card-band" viewBox="0 0 540 309" preserveAspectRatio="none" aria-hidden="true">
      <path d="M0,168 C170,162 370,118 540,52 L540,309 L0,309 Z" fill="var(--teal)"/>
      <path d="M150,156 C300,140 430,100 540,44 L540,50 C430,106 300,146 150,156 Z" fill="var(--teal)"/>
    </svg>
    <div class="brand">
      <span class="brand-dot"></span>
      <span class="brand-name">Halvorsen Dental Center</span>
    </div>
    <p class="services">
      Family Dentistry • Crowns/Bridges<br>
      Cosmetic • Implants/Tooth Replacement<br>
      Whitening • Dentures<br>
      Tooth Colored Fillings • Root Canals
    </p>
  </section>

  <section class="card card--front" aria-label="Card front – contact">
    <div class="brand">
      <span class="brand-dot"></span>
      <span class="brand-name">Halvorsen Dental Center</span>
    </div>
    <p class="doctor">Martin L. Halvorsen, D.D.S.</p>
    <ul class="contact">
      <li><b>p</b>(719) 482-6130</li>
      <li><b>e</b>halvorsendentalcenter@mailbox-example.net</li>
      <li><b>w</b>www.halvorsendentalcenter.example</li>
    </ul>
    <address class="address">
      <svg width="16" height="14" viewBox="0 0 16 14" aria-hidden="true">
        <path d="M8 0 L16 7 L14 7 L14 14 L10 14 L10 9 L6 9 L6 14 L2 14 L2 7 L0 7 Z" fill="var(--text-blue)"/>
      </svg>
      <span>7234 Pinewick Ave. Suite B<br>Colorado Springs<br>CO 80547</span>
    </address>
  </section>

</body>
</html>
```